Values and Organizational Purpose Signage

We recently solidified our company values, organizatioanal purpose and strategic vision. I'd like to develop some tasteful (not overly corporate) signage of these values to display in our office.

I've attached the hand-written values and purpose that my core team members then initialed acknowleding they align along with the signage at the front of our office to provide some perspective on our brand identity.

Industry/Entity Type

It Company

Font styles to use
Sans Serif

Requirements
Must have
• I'd like to see the values and org purpose depicted as one sign and as separate signs (i.e., values on one sign and org purpose on another). I need it to reflect our brand identity which I've uploaded

```html
<!DOCTYPE html>
<html lang="en">
<head>
<meta charset="UTF-8">
<title>Organizational Purpose and Core Values Sign</title>
<link rel="stylesheet" href="https://fonts.googleapis.com/css2?family=Montserrat:wght@700;800&family=Roboto:wght@400&display=swap">
<style>
  :root {
    --ink: #00303a;
    --leaf: #74a01f;
    --paper: #ffffff;
    --backdrop: #ececec;
    --body-text: #1d2b30;
  }
  * { margin: 0; padding: 0; box-sizing: border-box; }
  html, body {
    width: 1200px;
    height: 748px;
    overflow: hidden;
    background: var(--backdrop);
  }
  .canvas {
    position: relative;
    width: 1200px;
    height: 748px;
  }
  .sign {
    position: absolute;
    left: 165px;
    top: 27px;
    width: 869px;
    height: 693px;
    background: var(--paper);
    box-shadow: 0 6px 18px rgba(0,0,0,0.18);
  }
  .mount-points {
    position: absolute;
    inset: 0;
  }
  .heading-bar {
    position: absolute;
    left: 52px;
    width: 758px;
    height: 50px;
    background: var(--ink);
    color: var(--paper);
    font-family: "Montserrat", sans-serif;
    font-weight: 800;
    font-size: 41px;
    line-height: 50px;
    text-align: center;
    letter-spacing: 0.2px;
  }
  .heading-bar--purpose { top: 65px; }
  .heading-bar--values { top: 200px; }
  .purpose-statement {
    position: absolute;
    left: 52px;
    top: 128px;
    width: 758px;
    text-align: center;
    font-family: "Roboto", sans-serif;
    font-size: 25px;
    color: var(--body-text);
  }
  .value {
    position: absolute;
    left: 52px;
    width: 760px;
    display: flex;
    align-items: flex-start;
  }
  .value-name {
    flex: 0 0 306px;
    height: 47px;
    background: var(--ink);
    color: var(--leaf);
    font-family: "Montserrat", sans-serif;
    font-weight: 700;
    font-size: 25px;
    line-height: 47px;
    text-align: right;
    padding-right: 11px;
    white-space: nowrap;
  }
  .value-text {
    margin-left: 22px;
    font-family: "Roboto", sans-serif;
    font-size: 21px;
    line-height: 27px;
    color: var(--body-text);
  }
  .value--respect { top: 288px; }
  .value--respect .value-text { margin-top: -4px; }
  .value--integrity { top: 382px; }
  .value--integrity .value-text { margin-top: 10px; }
  .value--excellence { top: 477px; }
  .value--excellence .value-text { margin-top: 2px; }
  .value--open { top: 571px; }
  .value--open .value-text { margin-top: -1px; }
</style>
</head>
<body>
<main class="canvas">
  <section class="sign">
    <svg class="mount-points" width="869" height="693" viewBox="0 0 869 693" aria-hidden="true">
      <circle cx="31" cy="27" r="11" fill="#00303a"/>
      <circle cx="839" cy="27" r="11" fill="#00303a"/>
      <circle cx="31" cy="664" r="11" fill="#00303a"/>
      <circle cx="839" cy="664" r="11" fill="#00303a"/>
    </svg>

    <h1 class="heading-bar heading-bar--purpose">ORGANIZATIONAL PURPOSE</h1>
    <p class="purpose-statement">We deliver simple and digestible solutions to complex matters</p>

    <h2 class="heading-bar heading-bar--values">CORE VALUES DEFINED</h2>

    <div class="value value--respect">
      <span class="value-name">RESPECT</span>
      <p class="value-text">We are transparent and receptive to the<br>thoughts, opinion and feelings of others</p>
    </div>
    <div class="value value--integrity">
      <span class="value-name">INTEGRITY</span>
      <p class="value-text">We uphold our promises</p>
    </div>
    <div class="value value--excellence">
      <span class="value-name">EXCELLENCE</span>
      <p class="value-text">We continuously strive to be the best in<br>all endeavors</p>
    </div>
    <div class="value value--open">
      <span class="value-name">OPEN MINDEDNESS</span>
      <p class="value-text">We encourage creative and innovative<br>expressions</p>
    </div>
  </section>
</main>
</body>
</html>
```